Roofing Company Truck Wrap Design

We are looking for a clean, modern design for our fleet of trucks. Our trucks are white Varden trucks. We want them to be clean and modern, yet well branded and be able to stand out on the road.
Products and services we want to be written on the truck are:
Tile - Metal - Shingle - Coatings - Flat Roofs
We would want our phone number 505-617-2381, along with our website www.quillbrook-roofing.com.
We also would need our license number reading "BLU #517260".
The orange color in our logo should be pantone 2028C. We would prefer to use a black background behind the logos and phone numbers with white writing so it stands out, with accent colors using the orange from the logo.
Other font styles liked:
- Match font from logo
Colors

```html
<!DOCTYPE html>
<html lang="en">
<head>
<meta charset="utf-8">
<title>Quillbrook Roofing – Truck Wrap</title>
<link rel="stylesheet" href="https://fonts.googleapis.com/css2?family=Oswald:wght@500&family=Poppins:wght@600&family=Roboto+Slab:wght@700&display=swap">
<style>
  :root {
    --wrap-black: #231f20;
    --wrap-orange: #e05a1c;
    --wrap-white: #ffffff;
    --glass: #8d8f93;
    --tyre: #1b1b1b;
    --well: #2e2e2e;
    --hub: #a7a9ac;
    --trim: #141414;
    --lamp: #5a1c1c;
    --shadow: #e6e6e6;
    --page: #ffffff;
  }
  html, body {
    margin: 0;
    width: 1200px;
    height: 1200px;
    overflow: hidden;
    background: var(--page);
  }
  .wrap-sheet { display: block; width: 1200px; height: 1200px; }
  .brand-name { font-family: "Roboto Slab", Georgia, serif; font-weight: 700; fill: var(--wrap-white); }
  .services { font-family: "Oswald", "Arial Narrow", sans-serif; font-weight: 500; fill: var(--wrap-white); letter-spacing: 0.5px; }
  .phone { font-family: "Poppins", Arial, sans-serif; font-weight: 600; letter-spacing: 1.5px; }
  .phone--white { fill: var(--wrap-white); }
  .phone--orange { fill: var(--wrap-orange); }
  .website { font-family: "Poppins", Arial, sans-serif; font-weight: 600; fill: var(--wrap-orange); }
  .license { font-family: "Oswald", "Arial Narrow", sans-serif; font-weight: 500; fill: var(--wrap-black); letter-spacing: 0.6px; }
  .dot { fill: var(--wrap-orange); }
  .body-base { fill: var(--wrap-white); }
  .panel-black { fill: var(--wrap-black); }
  .panel-orange { fill: var(--wrap-orange); }
  .panel-white { fill: var(--wrap-white); }
  .window { fill: var(--glass); }
  .trim { fill: var(--trim); }
  .lamp { fill: var(--lamp); }
  .ground-shadow { fill: var(--shadow); }
  .wheel-well { fill: var(--well); }
  .tyre { fill: var(--tyre); }
  .hub { fill: var(--hub); }
</style>
</head>
<body>
<svg class="wrap-sheet" viewBox="0 0 960 960" xmlns="http://www.w3.org/2000/svg">
  <defs>
    <path id="truck-body" d="M152,296 L160,276 Q172,268 230,266 L300,262 L340,232 Q360,218 385,212 L478,206 Q486,206 486,214 L486,262 L780,260 Q790,261 790,272 L792,335 L798,340 L798,358 L765,362 L702,362 A47,47 0 0 0 608,362 L298,366 A50,50 0 0 0 198,366 L152,364 L148,340 Z"/>
    <clipPath id="body-clip"><use href="#truck-body"/></clipPath>
    <g id="truck-parts-back">
      <ellipse class="ground-shadow" cx="470" cy="412" rx="330" ry="9"/>
      <circle class="wheel-well" cx="248" cy="376" r="50"/>
      <circle class="wheel-well" cx="655" cy="374" r="49"/>
    </g>
    <g id="truck-parts-front">
      <polygon class="window" points="338,268 368,234 392,225 446,223 446,268"/>
      <path class="trim" d="M330,262 L352,258 L354,276 L334,278 Z"/>
      <rect class="trim" x="144" y="336" width="44" height="26" rx="4"/>
      <rect class="trim" x="156" y="290" width="16" height="40" rx="2"/>
      <rect class="lamp" x="782" y="280" width="10" height="36" rx="2"/>
      <rect class="trim" x="764" y="340" width="36" height="20" rx="3"/>
      <circle class="tyre" cx="248" cy="378" r="42"/><circle class="hub" cx="248" cy="378" r="20"/>
      <circle class="tyre" cx="655" cy="376" r="42"/><circle class="hub" cx="655" cy="376" r="20"/>
    </g>
  </defs>

  <!-- Layout A: black cab, white rocker with orange sweep -->
  <g class="truck truck--a">
    <use href="#truck-parts-back"/>
    <use href="#truck-body" class="body-base"/>
    <g clip-path="url(#body-clip)">
      <rect class="panel-black" x="140" y="190" width="670" height="220"/>
      <polygon class="panel-white" points="140,190 486,190 486,204 372,222 330,262 300,282 150,290"/>
      <polygon class="panel-orange" points="190,293 302,283 338,258 344,262 308,290 190,299"/>
      <polygon class="panel-orange" points="418,211 444,203 470,203 446,213"/>
      <polygon class="panel-white" points="486,366 560,318 810,314 810,410 486,410"/>
      <polygon class="panel-orange" points="486,350 548,320 810,304 810,313 556,327 486,362"/>
      <rect class="panel-white" x="300" y="349" width="190" height="30"/>
    </g>
    <use href="#truck-parts-front"/>

    <text class="brand-name" x="393" y="340" font-size="16" text-anchor="middle">Quillbrook Roofing</text>
    <text class="website" x="393" y="361" font-size="8.5" text-anchor="middle">www.quillbrook-roofing.com</text>
    <text class="services" x="500" y="278" font-size="11">TILE  METAL <tspan class="dot">•</tspan> SHINGLE <tspan class="dot">•</tspan> COATINGS <tspan class="dot">•</tspan> FLAT ROOFS</text>
    <text class="phone phone--white" x="555" y="298" font-size="18">505-617-2381</text>
    <text class="license" x="712" y="328" font-size="8">BLU #517260</text>
  </g>

  <!-- Layout B: black upper body, orange lower body -->
  <g class="truck truck--b" transform="translate(2,312)">
    <use href="#truck-parts-back"/>
    <use href="#truck-body" class="body-base"/>
    <g clip-path="url(#body-clip)">
      <rect class="panel-black" x="140" y="190" width="670" height="220"/>
      <polygon class="panel-white" points="140,190 486,190 486,204 372,222 330,262 300,282 150,290"/>
      <polygon class="panel-orange" points="190,293 302,283 338,258 344,262 308,290 190,299"/>
      <polygon class="panel-orange" points="140,355 300,352 486,336 560,316 810,300 810,410 140,410"/>
    </g>
    <use href="#truck-parts-front"/>

    <text class="brand-name" x="432" y="350" font-size="18" text-anchor="middle" transform="rotate(-5 432 350)">Quillbrook Roofing</text>
    <text class="phone phone--orange" x="588" y="277" font-size="14" transform="rotate(-3 588 277)">505-617-2381</text>
    <text class="services" x="545" y="311" font-size="10" transform="rotate(-3 545 311)">TILE <tspan class="dot">•</tspan> METAL <tspan class="dot">•</tspan> SHINGLE <tspan class="dot">•</tspan> COATINGS <tspan class="dot">•</tspan> FLAT ROOFS</text>
  </g>
</svg>
</body>
</html>
```